Iron and home washing service

I provide I home iron and washing service for adult and kids clothes on a smoke pet free environment. I can collect and offer a next day delivery. Or same day depend on items and volume. I offer competitive frendly and reliable service and price. I charge by weight £4,50 / kg. approx 5 items =1 kg minimum for collection.

```html
<!DOCTYPE html>
<html lang="en">
<head>
<meta charset="utf-8">
<title>Iron Service Flyer</title>
<link href="https://fonts.googleapis.com/css2?family=Roboto+Condensed:wght@700&family=Open+Sans:wght@400;600&display=swap" rel="stylesheet">
<style>
  :root {
    --blue-deep: #163f92;
    --blue-mid: #2561bd;
    --orange: #f39a1e;
    --orange-deep: #e97a12;
    --orange-light: #fbc04a;
    --white: #ffffff;
    --ink: #2a2a2a;
    --panel: #f1f2f4;
    --tick: #2a63b8;
  }
  * { margin: 0; padding: 0; box-sizing: border-box; }
  html, body { width: 900px; height: 1200px; overflow: hidden; background: var(--white); }
  .flyer { position: relative; width: 900px; height: 1200px; overflow: hidden; background: var(--white); font-family: "Open Sans", sans-serif; }
  .flyer-shapes { position: absolute; inset: 0; }
  .hero-photo {
    position: absolute; left: 290px; top: 50px; width: 590px; height: 300px;
    border-radius: 20px;
    background: linear-gradient(100deg, #d8eef8 0%, #b9dcf0 30%, #f6a9c8 55%, #8fd0ee 72%, #f3a447 86%, #e65a8a 100%);
    opacity: .85;
  }
  .sticker {
    position: absolute; left: 40px; top: 15px; width: 230px; height: 230px; border-radius: 50%;
    background: radial-gradient(circle at 40% 35%, var(--orange-light), var(--orange) 55%, var(--orange-deep));
    box-shadow: 0 4px 10px rgba(0,0,0,.25);
    display: flex; align-items: center; justify-content: center; text-align: center;
    font-family: "Roboto Condensed", sans-serif; font-weight: 700; color: var(--white);
    font-size: 33px; line-height: 1.18; text-shadow: 0 2px 3px rgba(0,0,0,.3);
  }
  .title {
    position: absolute; left: 0; right: 0; top: 420px; text-align: center;
    font-family: "Roboto Condensed", sans-serif; font-weight: 700; font-size: 118px; line-height: 1.2;
    color: var(--white); text-shadow: 0 4px 8px rgba(0,0,0,.35); letter-spacing: 1px;
  }
  .price-panel {
    position: absolute; left: 58px; top: 578px; width: 780px; height: 282px;
    background: linear-gradient(#ffffff, var(--panel)); border-radius: 18px;
    box-shadow: 0 5px 12px rgba(0,0,0,.3); overflow: hidden;
  }
  .price-panel-header {
    height: 56px; background: linear-gradient(var(--orange-light), var(--orange));
    color: var(--white); font-family: "Roboto Condensed", sans-serif; font-weight: 700;
    font-size: 27px; display: flex; align-items: center; justify-content: center;
    text-shadow: 0 1px 2px rgba(0,0,0,.3);
  }
  .price-list { list-style: none; padding: 20px 0 0 30px; }
  .price-list li {
    display: flex; align-items: center; gap: 12px; height: 48px;
    font-weight: 600; font-size: 27px; color: var(--ink);
  }
  .tick-box { width: 22px; height: 22px; flex: none; }
  .newborn-heading {
    position: absolute; left: 60px; top: 880px; color: var(--white);
    font-family: "Roboto Condensed", sans-serif; font-weight: 700; font-size: 27px; line-height: 1.3;
  }
  .newborn-list { position: absolute; left: 60px; top: 964px; list-style: none; color: var(--white); }
  .newborn-list li { display: flex; align-items: center; gap: 14px; font-size: 19px; height: 29px; }
  .newborn-list li.highlight { font-weight: 600; font-size: 24px; height: 34px; }
  .bullet {
    width: 20px; height: 20px; border-radius: 50%; flex: none;
    background: radial-gradient(circle, var(--white) 0 30%, var(--orange) 32%);
  }
  .call {
    position: absolute; right: 60px; top: 1136px; color: var(--ink); line-height: 1.2;
    font-family: "Roboto Condensed", sans-serif; font-weight: 700; font-size: 29px;
  }
  .call-number { font-size: 40px; margin-left: 6px; }
</style>
</head>
<body>
<div class="flyer">
  <svg class="flyer-shapes" width="900" height="1200" viewBox="0 0 900 1200">
    <defs>
      <linearGradient id="blueBand" x1="0" y1="0" x2="1" y2="0">
        <stop offset="0" stop-color="#163f92"/>
        <stop offset="0.5" stop-color="#2a66c2"/>
        <stop offset="1" stop-color="#163f92"/>
      </linearGradient>
      <linearGradient id="orangeBand" x1="0" y1="0" x2="1" y2="0">
        <stop offset="0" stop-color="#fbc04a"/>
        <stop offset="1" stop-color="#ef8317"/>
      </linearGradient>
      <pattern id="stripes" width="60" height="10" patternUnits="userSpaceOnUse">
        <rect x="0" width="14" height="10" fill="#ffffff" opacity="0.05"/>
        <rect x="30" width="6" height="10" fill="#ffffff" opacity="0.04"/>
      </pattern>
    </defs>
    <path class="blue-band" d="M0 395 C 250 340 600 345 900 400 L900 1112 C 600 1098 300 1094 0 1118 Z" fill="url(#blueBand)"/>
    <path d="M0 395 C 250 340 600 345 900 400 L900 1112 C 600 1098 300 1094 0 1118 Z" fill="url(#stripes)"/>
    <path class="top-accent" d="M0 378 C 250 325 600 330 900 392" fill="none" stroke="#f39a1e" stroke-width="8"/>
    <path d="M0 390 C 260 340 600 340 900 398" fill="none" stroke="#ffffff" stroke-width="3" opacity=".8"/>
    <path class="bottom-white" d="M0 1114 C 300 1094 600 1100 900 1108" fill="none" stroke="#ffffff" stroke-width="8"/>
    <path class="bottom-orange" d="M0 1126 C 300 1108 600 1130 900 1112 L900 1200 L0 1200 Z" fill="url(#orangeBand)"/>
  </svg>

  <div class="hero-photo" role="img" aria-label="Photo of a steam iron beside a stack of colourful folded towels with flowers"></div>

  <div class="sticker">Special<br>Service For<br>Newborn<br>Babys</div>

  <h1 class="title">Iron Service</h1>

  <section class="price-panel">
    <div class="price-panel-header">With the option do drop and collect by customer price</div>
    <ul class="price-list">
      <li><svg class="tick-box" viewBox="0 0 22 22"><rect x="1.5" y="3.5" width="16" height="16" fill="none" stroke="#2a63b8" stroke-width="2"/><path d="M5 11 L9 15 L20 2" fill="none" stroke="#2a63b8" stroke-width="3"/></svg>£8 pounds for 10 garments</li>
      <li><svg class="tick-box" viewBox="0 0 22 22"><rect x="1.5" y="3.5" width="16" height="16" fill="none" stroke="#2a63b8" stroke-width="2"/><path d="M5 11 L9 15 L20 2" fill="none" stroke="#2a63b8" stroke-width="3"/></svg>£20 pounds 25 garments</li>
      <li><svg class="tick-box" viewBox="0 0 22 22"><rect x="1.5" y="3.5" width="16" height="16" fill="none" stroke="#2a63b8" stroke-width="2"/><path d="M5 11 L9 15 L20 2" fill="none" stroke="#2a63b8" stroke-width="3"/></svg>Optional wash and ironing please ask price</li>
      <li><svg class="tick-box" viewBox="0 0 22 22"><rect x="1.5" y="3.5" width="16" height="16" fill="none" stroke="#2a63b8" stroke-width="2"/><path d="M5 11 L9 15 L20 2" fill="none" stroke="#2a63b8" stroke-width="3"/></svg>Collection and delivery free on £25 pounds order</li>
    </ul>
  </section>

  <h2 class="newborn-heading">Special Service to welcome<br>your Newborn Baby for Busy Mothers</h2>
  <ul class="newborn-list">
    <li><span class="bullet"></span>Washing and Iron</li>
    <li><span class="bullet"></span>Sterlised on vaccum sealed bag to avoid contamination</li>
    <li class="highlight"><span class="bullet"></span>Price £20 pounds for 30 garments</li>
    <li><span class="bullet"></span>Collection and delivery free</li>
  </ul>

  <p class="call">Call today:<span class="call-number">020.555.0148</span></p>
</div>
</body>
</html>
```